UI design for an iOS(iPhone) photo editing app

This design contest is to design the UI/screenshots of an iOS(iPhone) app named "Vivid Lantern". Some minor design details are left out at this point as the mockup is still in progress. The icon of this app will be designed separately. The winner of this job will be selected to work on a long term basis as an iPad version and several updates will have to be designed as well as the Android version. Please take
this as a long term opportunity.
The photo app is called "Vivid Lantern". The design need to dynamic, different that stands out WITH a serious and polished look.
All the mockups and sample screenshots are attached for ease. Please thoroughly review them.
This app has the following screens:
1. Welcome screen(just a simple background will do now as icon will be put later).
2. Main Screen (or LightBox)
The background of this screen can be the same as the background of the welcome screen. It can be a wooden background OR a background of your
choice that fits and blends in the buttons and fonts/colors.
The main screen has this bars/buttons/options that has separate screens:
On top, menu bar:
has these buttons
settings on the left(icon)
in the middle, 3 buttons (please check lightbox mockup and lightbox sample pics)
on the right, share icon(check share screen sample)
Our share options:
"Share" button screenshot:
Our share options:
Save
Email
Copy
Snapmoor
Friendloom
Pixbarn
Chirpset
in the middle, just background where the pictures would appear later after importing
or saving
at the bottom bar:
3 buttons:
Camera Roll(on the left)
Camera Button(middle)
Advanced Button(on the right)
2 versions of this screenshot need to be designed.
1. regular version with all the options
2. regular version plus the "steam effect" button showing up on top of the "Advanced" button(mockup with red lines)
3 separate screenshots need to be designed for the options"
settings screenshot(please check sample):
Gift Vivid Lantern to a friend
Rate/review in the Appvault
(space in between...so they are grouped)
Geotagiing(on/off)
Captured photos get location-specific information(these lines in smaller fonts)
Launch in Capture Mode(on/off)
Vivid Lantern is automatically lauched in camera mode
Autosave to Camera Roll(on/off)
Captured photos are directly saved to camera roll
Reset All Tutorials
Tap to reset all the tutorials
In the "Steam Effect" screen, please check the mockup
Top Bar: lightbox button(to go back), heading and Done button
Middle: Steam background(provided)
Bottom bar:
refresh button
droplets(when clicked on/off options show up on top, please check mockup)
finger size(when clicked 3 options show up)
steam density(when clicked 3 options show up)
Please use the buttons for the droplets, finger size and steam density from the steam effects button image provided)
(and also the background of this screenshot(in the middle) would be a steam screen which is provided. Please use the
steam background provided and you need to use the background in the middle, just omit the top and the bottom bar from the image)
Now back to the main(lightbox screen):
When Clicked on the "Camera" in the middle of the bottom bar, the capture mode screen shows up.
Please refer to the mockup first
There you will see the cancel button on the left
camera button in the middle
a small settings button on the right
and a filters button on the right
and the filters bar on the top
ours need to like this
please refer to capture mode sample 1
please refer to capture mode sample 2
please refer to capture mode sample 3
normal
Grid
timer(5/15/30 secs)
Edit Screen(check sample)
Edit options
Adjust:(displayed on a bar)
1. Left
2. Right
3. Horizontal
4. Vertical
5. Straightening
Crop:
None
Original
Golden
Freeform
Square
3:2
4:3
4:6
5:7
8:10
16:9
Filters:(please note that this filter icon and the filter icon in the "capture mode" screenshot need to same)
(the filters are displayed on a bar, please check sample)
There is a sample picture that you need to put in the picture of the filters. It would be same picture in
every filter at this point.
00.None
0.Calibrate
1. aurora
2. drizzle
3. icicle
4. blizzard
5. calm
6. dew
7. knot
8. dry
9. eye
10. flurry
11. fog
12. frost
13. hail
14. haze
15. heat
16. humid
17. overcast
18. polar
19. thermal
20. trace
Editing options on top:(check sample)
Brightness
Contrast
Saturation
Textures:(dispalyed on a bar, check sample)
1.None
2.Bark
3.Grunge1
4.Grunge2
5.grunge3
6.Grunge4
7.Paper
8.Cardboard
9.Wood
10.Bokeh
11.Bricks
12.Metal
13.Asphalt
14.Pavement1
15.Pavement2
16.Paint1
17.Paint2
18.Rust
19.Towel
20.Stone1
21.Stone2
22.Wall
23.Urban1
24.Urban2
25.Urban3
26.Watercolor
Tilt-shift/Vignette:(check sample)
Borders:(check samples, at this point, we are working on them, you just need to make a bar that displays them)
1.None
2.
3.
4.
5.
6.
7.
8.
9.
10.
11.
12.
13.
14.
15.
16.
This is our primary design mockup. Upon selecting the final version, we will be working on some more and minor details(as
we are also working with the coders).
And there is a folder callled "app sample". Please take a look at it and think how our app can be different and stand out.
Thanks and feel free to contact me anytime if you have any questions. Looking forward to hearing from you and building a long term
relationship.
All camera app users who likes to edit their photos with cool tools.
Building

```html
<!DOCTYPE html>
<html lang="en">
<head>
<meta charset="utf-8">
<title>Vivid Lantern – Capture Mode, Timer</title>
<link rel="stylesheet" href="https://fonts.googleapis.com/css2?family=Open+Sans:wght@600;700;800&display=swap">
<style>
  :root {
    --concrete-light: #8a8a8a;
    --concrete-mid: #5e5e5e;
    --concrete-dark: #3a3a3a;
    --grid-line: rgba(235, 235, 235, 0.55);
    --chip-bg: rgba(28, 28, 28, 0.88);
    --chip-border: rgba(140, 140, 140, 0.45);
    --text-light: #ffffff;
    --bar-top: #ebe9e6;
    --bar-bottom: #cfccc8;
    --teal: #0d5b5b;
    --teal-rim: #d9d6d2;
    --button-dark: #4a4a4a;
    --icon-circle: #4c4c4c;
    --track: #161616;
  }
  * { box-sizing: border-box; margin: 0; padding: 0; }
  html, body { width: 800px; height: 1200px; overflow: hidden; background: #2c2c2c; }
  body { font-family: "Open Sans", Arial, sans-serif; color: var(--text-light); }

  .screen { position: relative; width: 800px; height: 1200px; overflow: hidden; }

  .viewfinder {
    position: absolute; inset: 0 0 129px 0;
    background:
      radial-gradient(ellipse at 55% 35%, var(--concrete-light) 0%, var(--concrete-mid) 55%, var(--concrete-dark) 100%);
  }

  .grid { position: absolute; inset: 0; width: 800px; height: 1071px; }

  .timer-chip {
    position: absolute; left: 332px; top: 534px; width: 134px; height: 132px;
    background: var(--chip-bg); border: 1px solid var(--chip-border); border-radius: 10px;
    text-align: center; box-shadow: 0 2px 6px rgba(0,0,0,.4);
  }
  .timer-chip .seconds { display: block; font-size: 72px; font-weight: 800; line-height: 1; margin-top: 16px; letter-spacing: -1px; }
  .timer-chip .label { display: block; font-size: 21px; font-weight: 700; margin-top: 6px; }

  .zoom-panel {
    position: absolute; left: 702px; top: 346px; width: 110px; height: 516px;
    background: rgba(50, 50, 50, 0.85); border: 1px solid var(--chip-border); border-radius: 12px;
  }
  .zoom-panel .zoom-value { position: absolute; left: 0; width: 98px; top: 26px; text-align: center; font-size: 25px; font-weight: 700; }
  .zoom-panel .zoom-value sup { font-size: 16px; }
  .zoom-track {
    position: absolute; left: 37px; top: 70px; width: 21px; height: 396px;
    background: var(--track); border-radius: 11px; box-shadow: inset 0 1px 4px rgba(0,0,0,.8);
  }
  .zoom-knob { position: absolute; left: 20px; top: 429px; }

  .timer-status {
    position: absolute; left: 284px; top: 919px; width: 232px; height: 70px;
    background: var(--chip-bg); border: 1px solid var(--chip-border); border-radius: 8px;
    font-size: 27px; font-weight: 600; display: flex; align-items: center; justify-content: center;
  }

  .control-bar {
    position: absolute; left: 0; bottom: 0; width: 800px; height: 129px;
    background: linear-gradient(var(--bar-top), var(--bar-bottom));
  }
  .shutter { position: absolute; left: 0; top: 1040px; }

  .cancel-button {
    position: absolute; left: 19px; top: 1100px; width: 130px; height: 70px;
    background: var(--button-dark); border-radius: 8px; border: 1px solid #3a3a3a;
    font-size: 27px; font-weight: 700; display: flex; align-items: center; justify-content: center;
  }
  .round-button { position: absolute; top: 1100px; width: 74px; height: 74px; }
  .settings-button { left: 594px; }
  .filters-button { left: 693px; }
</style>
</head>
<body>
<main class="screen">
  <div class="viewfinder" role="img" aria-label="Live camera preview showing a grey cracked concrete wall"></div>

  <svg class="grid" viewBox="0 0 800 1071" aria-hidden="true">
    <g stroke="var(--grid-line)" stroke-width="2">
      <line x1="264" y1="0" x2="264" y2="1071"/>
      <line x1="536" y1="0" x2="536" y2="1071"/>
      <line x1="0" y1="391" x2="800" y2="391"/>
      <line x1="0" y1="785" x2="800" y2="785"/>
    </g>
  </svg>

  <div class="timer-chip">
    <span class="seconds">15</span>
    <span class="label">Set timer</span>
  </div>

  <div class="zoom-panel">
    <div class="zoom-value">1.0<sup>x</sup></div>
    <div class="zoom-track"></div>
    <svg class="zoom-knob" width="58" height="58" viewBox="0 0 58 58" aria-hidden="true">
      <defs>
        <radialGradient id="knobMetal" cx="50%" cy="50%" r="50%">
          <stop offset="0" stop-color="#ffffff"/>
          <stop offset="0.6" stop-color="#d8d8d8"/>
          <stop offset="1" stop-color="#9a9a9a"/>
        </radialGradient>
      </defs>
      <circle cx="29" cy="29" r="27" fill="url(#knobMetal)" stroke="#777" stroke-width="1"/>
      <circle cx="29" cy="29" r="4" fill="#bdbdbd"/>
    </svg>
  </div>

  <div class="timer-status">Timer Active</div>

  <footer class="control-bar"></footer>

  <svg class="shutter" width="800" height="160" viewBox="0 1040 800 160" aria-label="Shutter">
    <circle cx="400" cy="1218" r="172" fill="var(--teal-rim)"/>
    <circle cx="400" cy="1218" r="168" fill="var(--teal)"/>
    <circle cx="400" cy="1116" r="56" fill="#2a2a2a" stroke="#9a9a9a" stroke-width="2"/>
    <circle cx="400" cy="1116" r="46" fill="#111"/>
    <circle cx="400" cy="1116" r="34" fill="none" stroke="#3f6d5a" stroke-width="5"/>
    <circle cx="400" cy="1116" r="26" fill="none" stroke="#7a3550" stroke-width="4"/>
    <circle cx="400" cy="1116" r="18" fill="#0a0a0a"/>
    <circle cx="390" cy="1106" r="5" fill="#cfd8ff" opacity="0.7"/>
  </svg>

  <div class="cancel-button">Cancel</div>

  <svg class="round-button settings-button" viewBox="0 0 74 74" aria-label="Settings">
    <circle cx="37" cy="37" r="37" fill="var(--icon-circle)"/>
    <g fill="#fff" transform="translate(37 37)">
      <rect x="-4" y="-19" width="8" height="38" rx="2"/>
      <rect x="-4" y="-19" width="8" height="38" rx="2" transform="rotate(45)"/>
      <rect x="-4" y="-19" width="8" height="38" rx="2" transform="rotate(90)"/>
      <rect x="-4" y="-19" width="8" height="38" rx="2" transform="rotate(135)"/>
      <circle r="14"/>
    </g>
    <circle cx="37" cy="37" r="6" fill="var(--icon-circle)"/>
  </svg>

  <svg class="round-button filters-button" viewBox="0 0 74 74" aria-label="Filters">
    <circle cx="37" cy="37" r="37" fill="var(--icon-circle)"/>
    <circle cx="37" cy="37" r="21" fill="#fff"/>
    <g stroke="var(--icon-circle)" stroke-width="3" fill="none" transform="translate(37 37)">
      <line x1="-6" y1="-21" x2="14" y2="-5"/>
      <line x1="-6" y1="-21" x2="14" y2="-5" transform="rotate(60)"/>
      <line x1="-6" y1="-21" x2="14" y2="-5" transform="rotate(120)"/>
      <line x1="-6" y1="-21" x2="14" y2="-5" transform="rotate(180)"/>
      <line x1="-6" y1="-21" x2="14" y2="-5" transform="rotate(240)"/>
      <line x1="-6" y1="-21" x2="14" y2="-5" transform="rotate(300)"/>
    </g>
  </svg>
</main>
</body>
</html>
```